Popcorn Bag design

We need package design for the launch of our popcorn. We have chosen Hawaiian salts - Red and Black Lava - as our salts. Based on that decision we want to take a bit of a aloha spirit on the bag. Not over the top, but clearly a Hawaiian feel.. Required a Big Kahuna, smiling and with one arm out with a hang loose hand. The basic design will be used for multiple flavors of popcorn and a larger and smaller bags.
Please see the attached word document with more information.
Popcorn flavors for the design
Alaea Hawaiian Red Sea Salt
Alaea Hawaiian Red Sea Salt and Black Pepper
Black Hawaiian Lava Salt on Blue Kernels
The winning design will include the following
Design for the overall package - front and back (we have provided some information for the front and back of the bag.
Big Kahuna (smiling, with one arm out showing the "hang loose" hand samples. File(s) attached.
We will upload our logo, nutrition label and other
The winner will provide the following files:
Front and back of design - artwork ready
Front transparent background
Back transparent background
Big Kahuna transparent background

```html
<!DOCTYPE html>
<html lang="en">
<head>
<meta charset="utf-8">
<title>Kernel Cove Popcorn – Bag Front</title>
<link rel="stylesheet" href="https://fonts.googleapis.com/css2?family=Lato:wght@700;900&family=Barlow+Condensed:wght@500;700&family=Yellowtail&display=swap">
<style>
  :root {
    --stage: #3a3a3c;
    --stripe-grey: #b2b6bd;
    --stripe-white: #f6f5f2;
    --brand-red: #e8333c;
    --navy: #1e2a47;
    --window: #e6e7ea;
    --white: #ffffff;
    --popcorn-light: #f7f3e8;
    --popcorn-mid: #e4dcc6;
    --tiki-light: #b08a5e;
    --tiki-dark: #5e4027;
  }
  html, body {
    margin: 0;
    width: 1200px;
    height: 924px;
    overflow: hidden;
    background: var(--stage);
  }
  .bag-front {
    position: absolute;
    left: 296px;
    top: 32px;
    width: 609px;
    height: 860px;
    box-shadow: 6px 8px 12px rgba(0,0,0,0.35);
  }
  .brand-name {
    font-family: "Lato", sans-serif;
    font-weight: 900;
    font-size: 66px;
    letter-spacing: 3px;
    fill: var(--brand-red);
  }
  .product-script {
    font-family: "Yellowtail", cursive;
    font-size: 118px;
    fill: var(--white);
  }
  .tagline {
    font-family: "Barlow Condensed", sans-serif;
    font-weight: 700;
    font-size: 22px;
    fill: var(--white);
  }
  .benefit-text {
    font-family: "Lato", sans-serif;
    font-weight: 700;
    font-size: 12.5px;
    fill: var(--navy);
  }
  .flavor-arc {
    font-family: "Lato", sans-serif;
    font-weight: 700;
    font-size: 16px;
    letter-spacing: 0.5px;
    fill: var(--white);
  }
  .claim-text, .net-weight {
    font-family: "Barlow Condensed", sans-serif;
    font-weight: 500;
    font-size: 17px;
    fill: var(--navy);
  }
  .claim-rule { stroke: var(--navy); stroke-width: 1; opacity: 0.6; }
</style>
</head>
<body>
<svg class="bag-front" viewBox="0 0 609 860" xmlns="http://www.w3.org/2000/svg">
  <defs>
    <linearGradient id="stripe-fade" x1="0" y1="0" x2="0" y2="1">
      <stop offset="0" stop-color="#ffffff" stop-opacity="0"/>
      <stop offset="1" stop-color="#ffffff" stop-opacity="1"/>
    </linearGradient>
    <linearGradient id="popcorn-tone" x1="0" y1="0" x2="0" y2="1">
      <stop offset="0" stop-color="#ffffff" stop-opacity="0"/>
      <stop offset="0.35" stop-color="var(--popcorn-light)"/>
      <stop offset="1" stop-color="var(--popcorn-mid)"/>
    </linearGradient>
    <linearGradient id="tiki-tone" x1="0" y1="0" x2="1" y2="1">
      <stop offset="0" stop-color="var(--tiki-light)"/>
      <stop offset="1" stop-color="var(--tiki-dark)"/>
    </linearGradient>
    <path id="flavor-curve" d="M170 540 Q 315 460 465 540"/>
  </defs>

  <!-- background stripes -->
  <g class="stripes">
    <rect width="609" height="860" fill="var(--stripe-white)"/>
    <rect x="0" width="55.7" height="860" fill="var(--stripe-grey)"/>
    <rect x="111.4" width="55.7" height="860" fill="var(--stripe-grey)"/>
    <rect x="222.8" width="55.7" height="860" fill="var(--stripe-grey)"/>
    <rect x="334.2" width="55.7" height="860" fill="var(--stripe-grey)"/>
    <rect x="445.6" width="55.7" height="860" fill="var(--stripe-grey)"/>
    <rect x="557" width="55.7" height="860" fill="var(--stripe-grey)"/>
    <rect y="320" width="609" height="160" fill="url(#stripe-fade)"/>
    <rect y="480" width="609" height="380" fill="#ffffff"/>
  </g>

  <!-- brand name -->
  <text class="brand-name" x="305" y="150" text-anchor="middle">KERNEL COVE</text>

  <!-- popcorn photo area -->
  <rect role="img" aria-label="Photo of fresh white popcorn" x="0" y="640" width="609" height="220" fill="url(#popcorn-tone)"/>

  <!-- navy label panel -->
  <rect class="label-panel" x="99" y="194" width="411" height="420" fill="var(--navy)"/>

  <!-- product window -->
  <ellipse class="product-window" cx="274" cy="650" rx="175" ry="114" fill="var(--window)"/>

  <text class="product-script" x="300" y="318" text-anchor="middle">Popcorn</text>
  <g transform="rotate(-6 375 362)">
    <text class="tagline" x="375" y="350" text-anchor="middle">TASTE THE</text>
    <text class="tagline" x="375" y="374" text-anchor="middle">DIFFERENCE</text>
  </g>

  <!-- benefit badges -->
  <g class="benefit">
    <path d="M139 426 H247 V470 Q247 485 232 485 H139 Z" fill="var(--white)"/>
    <circle cx="138" cy="425" r="19" fill="var(--navy)" stroke="var(--white)" stroke-width="2.5"/>
    <path d="M129 425 l6 6 l12 -12" fill="none" stroke="var(--white)" stroke-width="3" stroke-linecap="round" stroke-linejoin="round"/>
    <text class="benefit-text" text-anchor="middle"><tspan x="194" y="443">NATURALLY</tspan><tspan x="194" y="457">LOWER IN</tspan><tspan x="194" y="471">SODIUM</tspan></text>
  </g>
  <g class="benefit">
    <path d="M260 426 H368 V470 Q368 485 353 485 H260 Z" fill="var(--white)"/>
    <circle cx="259" cy="424" r="19" fill="var(--navy)" stroke="var(--white)" stroke-width="2.5"/>
    <path d="M250 424 l6 6 l12 -12" fill="none" stroke="var(--white)" stroke-width="3" stroke-linecap="round" stroke-linejoin="round"/>
    <text class="benefit-text" text-anchor="middle"><tspan x="315" y="443">HIGHER</tspan><tspan x="315" y="457">IN</tspan><tspan x="315" y="471">IRON</tspan></text>
  </g>
  <g class="benefit">
    <path d="M380 426 H489 V470 Q489 485 474 485 H380 Z" fill="var(--white)"/>
    <circle cx="380" cy="424" r="19" fill="var(--navy)" stroke="var(--white)" stroke-width="2.5"/>
    <path d="M371 424 l6 6 l12 -12" fill="none" stroke="var(--white)" stroke-width="3" stroke-linecap="round" stroke-linejoin="round"/>
    <text class="benefit-text" text-anchor="middle"><tspan x="435" y="443">SMOOTH</tspan><tspan x="435" y="457">RICH</tspan><tspan x="435" y="471">FLAVOR</tspan></text>
  </g>

  <!-- flavor name on arc -->
  <text class="flavor-arc"><textPath href="#flavor-curve" startOffset="50%" text-anchor="middle">ALAEA HAWAIIAN RED SEA SALT</textPath></text>

  <!-- mascot area -->
  <rect role="img" aria-label="Illustration of the smiling carved tiki Big Kahuna mascot" x="427" y="537" width="178" height="300" rx="14" fill="url(#tiki-tone)"/>

  <!-- claims list -->
  <g class="claims">
    <line class="claim-rule" x1="10" y1="735" x2="182" y2="735"/>
    <text class="claim-text" x="24" y="758">Big Kahuna Approved</text>
    <line class="claim-rule" x1="10" y1="769" x2="160" y2="769"/>
    <text class="claim-text" x="24" y="792">Popped with Aloha</text>
    <line class="claim-rule" x1="10" y1="802" x2="150" y2="802"/>
    <text class="claim-text" x="24" y="825">Gluten Free</text>
    <line class="claim-rule" x1="10" y1="836" x2="118" y2="836"/>
  </g>

  <text class="net-weight" x="247" y="832">Net weight 4.4oz</text>
</svg>
</body>
</html>
```